IT Consulting Business Card Design

We need a business card on our company name....which is a IT consulting and staffing company. We also train masters graduates in various IT courses. 70% of the time these cards will be handed out to the graduate students at the universities. 30% for our clients and business partners. We are uploading our company logo...would like to see something that matches our logo or blends with it. Please visit www.brivolentaxis.com for more details on logo and colors.

Target Market(s)

70% of the time these cards will be handed out to the graduate students at the universities. 30% for our clients and business partners.

Industry/Entity Type

Business

Contact Information for Business Card

Tomas Verlinde
Vice-President
Brivolen Taxis Inc
3187 Corwick Lane, Suite 412
Halden Park, OH 44910
tomas@brivolentaxis.com
Office : 1-855-555-0148 X 312
Cell number : 614-555-0193

Requirements
Nice to have
• may be company logo and name on the back of the card and detials on the other side...just a thought..!!

```html
<!DOCTYPE html>
<html lang="en">
<head>
<meta charset="utf-8">
<title>Brivolen Taxis – Business Card</title>
<link rel="stylesheet" href="https://fonts.googleapis.com/css2?family=PT+Sans:wght@400;700&family=PT+Sans+Narrow:wght@400;700&display=swap">
<style>
  :root {
    --page: #ffffff;
    --card-grey: #4a4a4c;
    --band-black: #161616;
    --accent-red: #e1222b;
    --text-white: #ffffff;
    --text-soft: #e4e4e4;
  }
  html, body {
    margin: 0;
    padding: 0;
    width: 1000px;
    height: 1200px;
    overflow: hidden;
    background: var(--page);
  }
  .canvas {
    position: relative;
    width: 1000px;
    height: 1200px;
  }
  .card {
    position: absolute;
    left: 80px;
    width: 840px;
    height: 490px;
    display: block;
    box-shadow: 0 2px 6px rgba(0,0,0,0.18);
  }
  .card--front { top: 85px; }
  .card--back  { top: 625px; }
  .card-base  { fill: var(--card-grey); }
  .band       { fill: var(--band-black); }
  .side-bar   { fill: var(--accent-red); }
  .logo-dot   { fill: var(--accent-red); }
  .wordmark {
    font-family: "PT Sans Narrow", sans-serif;
    font-weight: 700;
    fill: var(--text-white);
    letter-spacing: 0.2px;
  }
  .person-name {
    font-family: "PT Sans", sans-serif;
    font-weight: 700;
    fill: var(--text-white);
  }
  .person-title {
    font-family: "PT Sans", sans-serif;
    font-weight: 400;
    fill: var(--text-soft);
  }
  .detail {
    font-family: "PT Sans", sans-serif;
    font-weight: 400;
    fill: var(--text-white);
    font-size: 12px;
  }
</style>
</head>
<body>
<main class="canvas">

  <!-- Front side -->
  <svg class="card card--front" viewBox="0 0 434 253" aria-label="Business card front">
    <rect class="card-base" x="0" y="0" width="434" height="253"/>
    <rect class="band" x="0" y="50" width="434" height="117"/>
    <rect class="side-bar" x="0" y="33" width="36" height="188"/>
    <rect class="side-bar" x="398" y="33" width="36" height="188"/>
    <circle class="logo-dot" cx="116" cy="110" r="36"/>
    <text class="wordmark" x="166" y="118" font-size="24">BRIVOLEN TAXIS</text>
    <text class="person-name" x="354" y="199" font-size="16" text-anchor="end">Tomas Verlinde</text>
    <text class="person-title" x="354" y="215" font-size="11.5" text-anchor="end">Vice-President</text>
  </svg>

  <!-- Back side -->
  <svg class="card card--back" viewBox="0 0 434 253" aria-label="Business card back">
    <rect class="card-base" x="0" y="0" width="434" height="253"/>
    <rect class="band" x="0" y="69" width="434" height="90"/>
    <rect class="side-bar" x="0" y="33" width="36" height="188"/>
    <rect class="side-bar" x="398" y="33" width="36" height="188"/>
    <text x="91" y="45">
      <tspan class="person-name" font-size="16">Tomas Verlinde</tspan>
      <tspan class="person-title" font-size="14" dx="6">Vice-President</tspan>
    </text>
    <text class="wordmark" x="91" y="95" font-size="18">BRIVOLEN TAXIS</text>
    <text class="detail" x="91" y="118">3187 Corwick Lane,</text>
    <text class="detail" x="91" y="134">Suite 412 Halden Park,</text>
    <text class="detail" x="91" y="150">OH 44910</text>
    <circle class="logo-dot" cx="304" cy="114" r="32"/>
    <text class="detail" x="91" y="189">tomas@brivolentaxis.com</text>
    <text class="detail" x="91" y="206">Office : 1-855-555-0148 X 312</text>
    <text class="detail" x="91" y="223">Cell number : 614-555-0193</text>
  </svg>

</main>
</body>
</html>
```